Business Card Design Project - IT Company

CLOUD IT company working with medium to large corporate clients requires 2 sided Business Card design.

Strong, Professional and modern is what I am looking for.

The Logo JPG attached has all the colour palette options. which consist of Red and Silver on various backgrounds

Preferred option for the Back of card is either Silver Text on Red or Silver Text on Black. Though this is not concrete. Surprise me.

Logo must be prominent along with Contact details of the staff member

Tagline can be all Capitals " CLOUD MANAGED SERVICES"

I will look to provide feedback and tweaks to get the right design so it should be a fun process.

I will provide the layered files to the top few contenders.

Reason: Leaving the door open for some creativity. Don't forget this is an technology company. .

Target Market(s)

Leaders, decision makers, CEOs, CIOs,

Industry/Entity Type

Business

Requirements
Must have
• Data must have is

Company Name: Brelquist
Tagline: Cloud Managed Services

No Particular order

First Name Last name
Director
Mobile 0477 555 019
www.brelquist-example.com
First.Lastname@brelquist-example.com
Suite 7, 48 Wexmoor Lane, Sydney NSW 2000

```html
<!DOCTYPE html>
<html lang="en">
<head>
<meta charset="utf-8">
<title>Brelquist Business Card</title>
<link href="https://fonts.googleapis.com/css2?family=Jost:wght@400;500;600&display=swap" rel="stylesheet">
<style>
  :root {
    --stage: #1b1b1d;
    --card-black: #0c0c0d;
    --card-red: #c0161f;
    --card-red-deep: #a50f17;
    --silver: #d9dadc;
    --silver-dark: #8e9094;
    --text-light: #f3f3f3;
    --text-muted: #f2b9bc;
  }
  * { box-sizing: border-box; margin: 0; padding: 0; }
  html, body { width: 1200px; height: 832px; overflow: hidden; }
  body {
    background: var(--stage);
    font-family: "Jost", "Futura", sans-serif;
    position: relative;
  }
  .card {
    position: absolute;
    top: 261px;
    width: 540px;
    height: 310px;
    border-radius: 4px;
    overflow: hidden;
    box-shadow: 0 14px 36px rgba(0,0,0,0.55);
  }
  .card-back { left: 40px; background: var(--card-black); }
  .card-front { left: 620px; background: var(--card-red); }

  /* back */
  .back-brand {
    position: absolute;
    left: 70px;
    top: 118px;
    display: flex;
    align-items: center;
    gap: 14px;
  }
  .brand-dot {
    width: 34px; height: 34px;
    border-radius: 50%;
    border: 4px solid var(--silver);
    flex: none;
  }
  .brand-name {
    font-weight: 600;
    color: var(--silver);
    line-height: 1;
    white-space: nowrap;
  }
  .back-brand .brand-name { font-size: 48px; letter-spacing: 0.5px; }
  .back-tagline {
    position: absolute;
    left: 120px;
    top: 172px;
    font-size: 12px;
    letter-spacing: 2.2px;
    color: var(--silver);
    white-space: nowrap;
  }
  .back-accent {
    position: absolute;
    right: 56px;
    top: 168px;
    width: 64px; height: 64px;
    border-radius: 50%;
    border: 5px solid #2e2e31;
  }

  /* front */
  .front-arc { position: absolute; left: 0; top: 0; }
  .front-brand {
    position: absolute;
    left: 200px;
    top: 92px;
    display: flex;
    align-items: center;
    gap: 8px;
  }
  .front-brand .brand-dot { width: 20px; height: 20px; border-width: 3px; }
  .front-brand .brand-name { font-size: 28px; }
  .front-tagline {
    position: absolute;
    left: 230px;
    top: 124px;
    font-size: 7px;
    letter-spacing: 1.2px;
    color: var(--silver);
    white-space: nowrap;
  }
  .address {
    position: absolute;
    left: 192px;
    top: 140px;
    width: 184px;
    font-size: 10px;
    line-height: 1.3;
    color: var(--text-light);
    text-align: center;
    white-space: nowrap;
  }
  .phone {
    position: absolute;
    left: 192px;
    top: 176px;
    font-size: 24px;
    letter-spacing: 2px;
    color: var(--text-light);
    white-space: nowrap;
  }
  .person {
    position: absolute;
    right: 16px;
    top: 150px;
    color: var(--text-light);
  }
  .person-name { font-size: 14px; font-weight: 500; white-space: nowrap; }
  .person-role { font-size: 12px; color: var(--text-muted); }
  .links {
    position: absolute;
    right: 16px;
    top: 236px;
    font-size: 10px;
    line-height: 1.5;
    color: var(--text-light);
    white-space: nowrap;
  }
</style>
</head>
<body>

<section class="card card-back" aria-label="Card back">
  <div class="back-brand">
    <span class="brand-dot"></span>
    <span class="brand-name">Brelquist</span>
  </div>
  <p class="back-tagline">CLOUD MANAGED SERVICES</p>
  <span class="back-accent"></span>
</section>

<section class="card card-front" aria-label="Card front">
  <svg class="front-arc" width="540" height="310" viewBox="0 0 540 310" aria-hidden="true">
    <defs>
      <linearGradient id="silverBand" x1="0" y1="0" x2="1" y2="1">
        <stop offset="0" stop-color="#f4f4f5"/>
        <stop offset="0.5" stop-color="#9a9ca0"/>
        <stop offset="1" stop-color="#e2e3e5"/>
      </linearGradient>
    </defs>
    <circle cx="20" cy="30" r="160" fill="var(--card-red-deep)"/>
    <circle cx="20" cy="30" r="164" fill="none" stroke="url(#silverBand)" stroke-width="9"/>
    <circle cx="80" cy="110" r="26" fill="none" stroke="#b8141c" stroke-width="5"/>
  </svg>

  <div class="front-brand">
    <span class="brand-dot"></span>
    <span class="brand-name">Brelquist</span>
  </div>
  <p class="front-tagline">CLOUD MANAGED SERVICES</p>
  <p class="address">Suite 7, 48 Wexmoor Lane, Sydney<br>NSW 2000</p>
  <p class="phone">0477 555 019</p>

  <div class="person">
    <p class="person-name">First Name Last name</p>
    <p class="person-role">Director</p>
  </div>

  <div class="links">
    <p>www.brelquist-example.com</p>
    <p>First.Lastname@brelquist-example.com</p>
  </div>
</section>

</body>
</html>
```